Founder / concept developer needs business card // Consultant needs VCARD

I need a business card for me as a founding consultant in Berlin. I advise entrepreneurs, especially in the design of business ideas, business plans or financing applications. More information about this in the annexes. My USP: I design / structure complex ideas and projects convincingly so that my client is successful. I want to communicate professionalism, effectiveness and clarity. Colors like from the range BLACK-GRAY-GREEN. I am 27 years old, I have studied business for 7 years. Attachments: - Business card design (only idea, do not focus on it) - Website screenshot (only idea, do not focus on it)

Target Market(s)

Target group: Founder (20-50 yrs, m / w, needy, in "break-up phase") and CONTRACTOR / "financier" (30-55 yrs, m / w, often public service "routine-oriented"). The foundations are in quite different industries: digital, craft, tourism, retail, services, etc. Almost all German.

Industry/Entity Type

Consultant

Contact Information for Business Card

Lukas Brandvik
M. Sc., International Business Administration
Gründungsberater, Konzeptentwickler
www.falkenhorn-beratung.de
kontakt@falkenhorn-beratung.de
Tel. 0471 239 5518

Colors

Designer to choose colors to be used in the design.

Requirements
Must have
• Professionalism, persuasiveness, clarity
Nice to have
• memorability
Should not have
• Schnörkelei

```html
<!DOCTYPE html>
<html lang="de">
<head>
<meta charset="utf-8">
<title>Lukas Brandvik – Visitenkarte</title>
<link rel="stylesheet" href="https://fonts.googleapis.com/css2?family=Montserrat:wght@400;500&family=Roboto:wght@400&display=swap">
<style>
  :root {
    --stage: #2a2a2a;
    --card: #1c1c1c;
    --card-edge: #141414;
    --white: #f2f2f2;
    --grey-text: #a9a9a9;
    --rule: #bdbdbd;
    --green: #3aa64c;
    --puzzle-light: #e9e9e9;
    --puzzle-dark: #8e8e8e;
    --photo-light: #d6d6d6;
    --photo-dark: #7a7a7a;
  }
  * { box-sizing: border-box; margin: 0; padding: 0; }
  html, body { width: 1200px; height: 1200px; overflow: hidden; }
  body {
    background: var(--stage);
    font-family: "Roboto", Arial, sans-serif;
    position: relative;
  }
  .card {
    position: absolute;
    left: 150px;
    width: 900px;
    height: 500px;
    background: var(--card);
    box-shadow: 0 10px 30px rgba(0,0,0,.5);
    overflow: hidden;
  }
  .card--back { top: 70px; }
  .card--front { top: 630px; }

  /* back side */
  .brand {
    position: absolute; left: 0; right: 0; top: 150px;
    text-align: center;
  }
  .brand__square {
    display: block; margin: 0 auto 18px;
    width: 120px; height: 82px;
    border: 3px solid var(--green);
  }
  .brand__name {
    font-family: "Montserrat", Arial, sans-serif;
    font-weight: 400; font-size: 34px; letter-spacing: 3px;
    color: var(--white); text-transform: uppercase;
  }
  .brand__url {
    margin-top: 4px;
    font-family: "Montserrat", Arial, sans-serif;
    font-size: 19px; letter-spacing: 1.5px; color: var(--green);
  }

  /* front side */
  .puzzle-photo {
    position: absolute; left: 0; top: 0; width: 520px; height: 380px;
    background: radial-gradient(ellipse at 10% 30%, var(--puzzle-light) 0%, #cfcfcf 45%, var(--card) 75%);
  }
  .portrait {
    position: absolute; left: 640px; top: 95px; width: 220px; height: 160px;
    border: 3px solid #dcdcdc;
    background: linear-gradient(135deg, var(--photo-light), var(--photo-dark));
  }
  .identity {
    position: absolute; right: 40px; top: 282px; text-align: right;
  }
  .identity__name {
    font-family: "Montserrat", Arial, sans-serif; font-weight: 500;
    font-size: 30px; letter-spacing: 2px; color: var(--white);
    text-transform: uppercase;
  }
  .identity__role {
    font-size: 19px; line-height: 27px; color: var(--grey-text);
  }
  .divider {
    position: absolute; left: 0; right: 40px; top: 398px;
    height: 3px; background: var(--rule);
  }
  .contacts {
    position: absolute; left: 45px; top: 404px;
    list-style: none; font-size: 19px; color: var(--white);
  }
  .contacts li { display: flex; align-items: center; gap: 12px; line-height: 28px; }
  .contacts svg { width: 18px; height: 18px; flex: none; }
  .phone {
    position: absolute; right: 60px; top: 420px;
    font-family: "Montserrat", Arial, sans-serif; font-size: 26px;
    letter-spacing: 1px; color: var(--white);
  }
  .phone__label { color: var(--green); margin-right: 6px; }
  .accent-band {
    position: absolute; left: 0; right: 0; bottom: 0; height: 26px;
    background: var(--green);
  }
</style>
</head>
<body>

<section class="card card--back" aria-label="Rückseite">
  <div class="brand">
    <span class="brand__square"></span>
    <div class="brand__name">Lukas Brandvik</div>
    <div class="brand__url">www.falkenhorn-beratung.de</div>
  </div>
</section>

<section class="card card--front" aria-label="Vorderseite">
  <div class="puzzle-photo" role="img" aria-label="Foto: weiße Puzzleteile mit einem einzelnen losen Teil auf dunklem Grund"></div>
  <div class="portrait" role="img" aria-label="Porträtfoto des Beraters in Schwarzweiß"></div>

  <div class="identity">
    <div class="identity__name">Lukas Brandvik</div>
    <div class="identity__role">M. Sc., International Business Administration</div>
    <div class="identity__role">Gründungsberater, Konzeptentwickler</div>
  </div>

  <div class="divider"></div>

  <ul class="contacts">
    <li>
      <svg viewBox="0 0 18 18" aria-hidden="true"><rect x="1" y="3.5" width="16" height="11" fill="var(--green)"/><path d="M1 3.5 L9 10 L17 3.5" fill="none" stroke="var(--card)" stroke-width="1.5"/></svg>
      kontakt@falkenhorn-beratung.de
    </li>
    <li>
      <svg viewBox="0 0 18 18" aria-hidden="true"><circle cx="9" cy="9" r="8" fill="var(--green)"/><path d="M1 9 H17 M9 1 C5 5 5 13 9 17 M9 1 C13 5 13 13 9 17" fill="none" stroke="var(--card)" stroke-width="1.2"/></svg>
      www.falkenhorn-beratung.de
    </li>
  </ul>

  <div class="phone"><span class="phone__label">Tel:</span>0471 239 5518</div>

  <div class="accent-band"></div>
</section>

</body>
</html>
```